Need a business card for our overland brand!

We had the logo made and we need a great design for our business card. Use the logo provide or tweak it however you see fit.

Contact Information for Business Card

Name, Title, Telephone, email, website

```html
<!DOCTYPE html>
<html lang="en">
<head>
<meta charset="utf-8">
<title>Ridgeway Trails – Business Card</title>
<link href="https://fonts.googleapis.com/css2?family=Montserrat:wght@400;500;700;800&display=swap" rel="stylesheet">
<style>
  :root {
    --navy: #22364e;
    --sky: #29a8e0;
    --mist: #e2e3e5;
    --paper: #f7f7f8;
    --paper-shade: #ececed;
    --stage: #f4f4ee;
    --white: #ffffff;
    --rule: #8d96a3;
    --icon-fill: #e9eaec;
  }
  * { margin: 0; padding: 0; box-sizing: border-box; }
  html, body { width: 1200px; height: 960px; overflow: hidden; }
  body {
    background: var(--stage);
    font-family: "Montserrat", sans-serif;
    display: flex;
    flex-direction: column;
    align-items: center;
    justify-content: center;
    gap: 60px;
  }
  .card {
    position: relative;
    width: 620px;
    height: 354px;
    overflow: hidden;
    background: linear-gradient(180deg, var(--white) 0%, var(--paper) 60%, var(--paper-shade) 100%);
    box-shadow: 0 6px 18px rgba(30, 40, 55, 0.12);
  }
  .card-shapes { position: absolute; inset: 0; width: 100%; height: 100%; }
  .brand-name {
    position: absolute;
    font-weight: 800;
    color: var(--navy);
    text-transform: uppercase;
    line-height: 0.95;
    letter-spacing: 0.5px;
    text-align: center;
  }
  .card-front .brand-name {
    left: 0; right: 0; top: 120px;
    font-size: 44px;
  }
  .card-back .brand-name {
    left: 36px; top: 112px;
    font-size: 30px;
    text-align: left;
  }
  .contact-panel {
    position: absolute;
    left: 300px; top: 58px;
    width: 290px;
    color: var(--white);
  }
  .person {
    display: flex;
    align-items: center;
    gap: 12px;
  }
  .person-icon { width: 20px; height: 22px; flex: none; }
  .person-name {
    font-size: 21px;
    font-weight: 400;
    letter-spacing: 1px;
    text-transform: uppercase;
  }
  .person-name strong { font-weight: 800; }
  .person-title {
    margin: 2px 0 0 32px;
    font-size: 15px;
    font-weight: 500;
    letter-spacing: 0.6px;
  }
  .divider {
    height: 1.5px;
    background: var(--rule);
    margin: 12px 0 20px 0;
    width: 270px;
  }
  .contact-list { list-style: none; }
  .contact-item {
    display: flex;
    align-items: center;
    gap: 14px;
    font-size: 14px;
    font-weight: 500;
    letter-spacing: 0.8px;
    margin-bottom: 12px;
  }
  .contact-icon {
    width: 24px; height: 24px;
    flex: none;
  }
</style>
</head>
<body>

  <!-- Front of card -->
  <section class="card card-front" aria-label="Business card front">
    <svg class="card-shapes" viewBox="0 0 620 354" preserveAspectRatio="none" aria-hidden="true">
      <polygon points="0,0 205,0 0,50" fill="var(--navy)"/>
      <polygon points="0,50 205,0 0,105" fill="var(--sky)"/>
      <polygon points="0,105 205,0 0,175" fill="var(--mist)"/>
      <polygon points="620,354 415,354 620,304" fill="var(--navy)"/>
      <polygon points="620,304 415,354 620,249" fill="var(--sky)"/>
      <polygon points="620,249 415,354 620,179" fill="var(--mist)"/>
    </svg>
    <div class="brand-name">Ridgeway<br>Trails</div>
  </section>

  <!-- Back of card -->
  <section class="card card-back" aria-label="Business card back">
    <svg class="card-shapes" viewBox="0 0 620 354" preserveAspectRatio="none" aria-hidden="true">
      <polygon points="262,0 300,0 150,354 130,354" fill="var(--sky)"/>
      <polygon points="300,0 620,0 620,354 150,354" fill="var(--navy)"/>
    </svg>

    <div class="brand-name">Ridgeway<br>Trails</div>

    <div class="contact-panel">
      <div class="person">
        <svg class="person-icon" viewBox="0 0 20 22" aria-hidden="true">
          <circle cx="10" cy="6" r="5" fill="var(--rule)"/>
          <path d="M0 22 V18 Q0 13 6 13 H14 Q20 13 20 18 V22 Z" fill="var(--rule)"/>
        </svg>
        <p class="person-name"><strong>Marcus</strong> Hale</p>
      </div>
      <p class="person-title">Marketing Manager</p>
      <div class="divider"></div>

      <ul class="contact-list">
        <li class="contact-item">
          <svg class="contact-icon" viewBox="0 0 24 24" aria-hidden="true">
            <circle cx="12" cy="12" r="12" fill="var(--icon-fill)"/>
            <path d="M9 7 L11 9.5 L10 11 Q11 13 13 14 L14.5 13 L17 15 L16 17 Q11 17 7 12 Q7 9 9 7 Z" fill="var(--navy)"/>
          </svg>
          <span>+015 4410 728391</span>
        </li>
        <li class="contact-item">
          <svg class="contact-icon" viewBox="0 0 24 24" aria-hidden="true">
            <circle cx="12" cy="12" r="12" fill="var(--icon-fill)"/>
            <path d="M12 5 Q7 5 7 10 Q7 13 12 19 Q17 13 17 10 Q17 5 12 5 Z" fill="var(--navy)"/>
            <circle cx="12" cy="10" r="2" fill="var(--icon-fill)"/>
          </svg>
          <span>B.4-Riverside Lane,Northgate</span>
        </li>
        <li class="contact-item">
          <svg class="contact-icon" viewBox="0 0 24 24" aria-hidden="true">
            <circle cx="12" cy="12" r="12" fill="var(--icon-fill)"/>
            <circle cx="12" cy="12" r="6" fill="none" stroke="var(--navy)" stroke-width="1.4"/>
            <path d="M6 12 H18 M12 6 Q9 12 12 18 M12 6 Q15 12 12 18" fill="none" stroke="var(--navy)" stroke-width="1.2"/>
          </svg>
          <span>www.yourwebsite.com</span>
        </li>
        <li class="contact-item">
          <svg class="contact-icon" viewBox="0 0 24 24" aria-hidden="true">
            <circle cx="12" cy="12" r="12" fill="var(--icon-fill)"/>
            <rect x="6" y="8" width="12" height="8" fill="none" stroke="var(--navy)" stroke-width="1.3"/>
            <path d="M6 8 L12 13 L18 8" fill="none" stroke="var(--navy)" stroke-width="1.3"/>
          </svg>
          <span>hello@yourgmail.com</span>
        </li>
      </ul>
    </div>
  </section>

</body>
</html>
```